Cover page and letterhead for athlete development program

We require an exciting and dynamic cover page with a second page letterhead in a word doc format for us to use as professional stationery for letter merges and portfolio documents. We are an athlete preparation company that specialises in training up and coming sports representatives in the fitness and sports science industry. We work with athletes from ages 13 - 24 mainly. If we could have images on the cover page from the sports of:
Rugby League
Rugby Union
Hockey
Cricket
AFL
Soccer
Track and Field
Netball
Basketball
Golf
Weight training

This would be a great start. Thank you

```html
<!DOCTYPE html>
<html lang="en">
<head>
<meta charset="utf-8">
<title>Summit Athletic Stationery</title>
<link rel="stylesheet" href="https://fonts.googleapis.com/css2?family=Montserrat:wght@600;700&family=Tinos&display=swap">
<style>
  :root {
    --backdrop: #7d878d;
    --paper-shade: #e6e6e6;
    --paper: #ffffff;
    --ink: #111111;
    --brand-black: #0b0b0b;
    --brand-gold: #c08a45;
    --brand-bronze: #8a5a2e;
  }
  * { margin: 0; padding: 0; box-sizing: border-box; }
  html, body { width: 1200px; height: 741px; overflow: hidden; }
  body { background: var(--backdrop); position: relative; font-family: "Tinos", "Times New Roman", serif; color: var(--ink); }

  .sheet {
    position: absolute;
    background: linear-gradient(100deg, var(--paper-shade) 0%, #f4f4f4 55%, var(--paper) 100%);
    overflow: hidden;
  }
  .letterhead { left: 123px; top: 41px; width: 444px; height: 628px; }
  .cover { left: 629px; top: 42px; width: 442px; height: 624px; }

  .brand {
    position: absolute;
    display: flex;
    align-items: center;
    font-family: "Montserrat", sans-serif;
    font-weight: 700;
    color: var(--brand-black);
    letter-spacing: 0.04em;
    text-transform: uppercase;
    white-space: nowrap;
  }
  .brand-square { background: var(--brand-black); flex: none; }
  .letterhead .brand { right: 35px; top: 49px; font-size: 14px; gap: 7px; }
  .letterhead .brand-square { width: 16px; height: 16px; }
  .cover .brand { left: 148px; top: 141px; font-size: 16px; gap: 8px; }
  .cover .brand-square { width: 19px; height: 19px; }

  .letter { position: absolute; left: 52px; top: 132px; width: 336px; font-size: 10px; line-height: 10.7px; }
  .letter p { margin-bottom: 10.7px; }
  .letter .gap-lg { margin-bottom: 21px; }
  .indent { padding-left: 5px; }
  .signer { padding-left: 18px; }

  .footer-contact, .footer-office {
    position: absolute;
    font-family: "Montserrat", sans-serif; font-weight: 600;
    font-size: 5px; line-height: 7px; text-align: right; white-space: nowrap;
  }
  .footer-contact { right: 151px; top: 590px; }
  .footer-office { right: 37px; top: 581px; }
  .footer-office .office-name {
    font-size: 7px; letter-spacing: 0.2em; line-height: 10px; font-weight: 700;
    text-transform: uppercase; margin-right: -0.2em;
  }

  .base-band { position: absolute; left: 0; bottom: 0; width: 100%; height: 10px; }

  .sports-collage {
    position: absolute; left: 66px; top: 241px; width: 327px; height: 161px;
    background: linear-gradient(110deg, #9c8a7a 0%, #5e6a72 35%, #b8763f 60%, #3f5e86 100%);
  }
</style>
</head>
<body>
  <section class="sheet letterhead">
    <div class="brand"><span class="brand-square"></span>Summit Athletic</div>

    <div class="letter">
      <p>Norwalk, CT 06850</p>
      <p class="gap-lg">June 28, 2007</p>
      <p class="gap-lg">Ms. Clara Whitfield<br>Halden Fellowship<br><span class="indent">48 Linden Street</span><br>Hartford, CT 06103</p>
      <p>Dear Ms. Whitfield:</p>
      <p class="gap-lg">The Halden Fellowship has always loomed on the horizon for me. Ever since I decided to major in history, I have wanted to participate in your program. From the research that I have done, I believe that your program provides its participants with an extensively detailed look at the history of the world through hands-on experience with fossils, artifacts, and other remains that compose the blueprint of our existence. &nbsp;I am applying for the Halden Fellowship because I believe that it would benefit me throughout my career and allow me to further understand the ideas behind history and how it is constructed.</p>
      <p>I believe my skills, experience, and goals make me an excellent candidate for your program.</p>
      <p class="gap-lg">Thank you very much for considering me for the Halden Fellowship. I am looking forward to hearing from you.</p>
      <p>Sincerely,</p>
      <p><span class="signer">Dana Kerr</span><br>(555) 014-2287</p>
    </div>

    <div class="footer-contact">
      Tel: (555) 018 4421 ext. 201<br>M (555) 017 3390<br>E info@summitathletic.co
    </div>
    <div class="footer-office">
      <div class="office-name">Summit Athletic</div>
      Cedar Business Park<br>12 Harbour Road, Eastgate<br>Port Alden, Northland
    </div>

    <svg class="base-band" viewBox="0 0 444 10" preserveAspectRatio="none" aria-hidden="true">
      <defs>
        <linearGradient id="goldLineA" x1="0" x2="1">
          <stop offset="0" stop-color="#e0a24f"/><stop offset="1" stop-color="#8a5a2e"/>
        </linearGradient>
      </defs>
      <polygon points="0,0 259,0 254,10 0,10" fill="#0b0b0b"/>
      <rect x="254" y="6.5" width="190" height="3.5" fill="url(#goldLineA)"/>
    </svg>
  </section>

  <section class="sheet cover">
    <div class="brand"><span class="brand-square"></span>Summit Athletic</div>
    <div class="sports-collage" role="img" aria-label="Collage of sports photography: rugby, ice hockey, cricket, basketball and soccer action shots"></div>

    <svg class="base-band" viewBox="0 0 442 10" preserveAspectRatio="none" aria-hidden="true">
      <defs>
        <linearGradient id="goldLineB" x1="0" x2="1">
          <stop offset="0" stop-color="#e0a24f"/><stop offset="1" stop-color="#8a5a2e"/>
        </linearGradient>
      </defs>
      <polygon points="0,0 258,0 253,10 0,10" fill="#0b0b0b"/>
      <rect x="253" y="6.5" width="189" height="3.5" fill="url(#goldLineB)"/>
    </svg>
  </section>
</body>
</html>
```